Australian Recruitment Agency Flyer

We are looking for a 1 page flyer to promote our recruitment company. We would like this to have a corporate look.

Attached is a word document with the content we would like included in the flyer.

I have also attached some of our clients logos to be included in the flyer

Target Market(s)

Professional organisations looking to hire new staff

Industry/Entity Type

It Company

Colors
85abd2
3176b5
31b7a3
d2a4cc
e667a6
b768aa
876aae
3276b5
f04a50

Requirements
Must have
• Must have the content that we have include on a word document in the design brief.

```html
<!DOCTYPE html>
<html lang="en">
<head>
<meta charset="utf-8">
<title>TalentHarbor – Recruitment Flyer</title>
<link rel="stylesheet" href="https://fonts.googleapis.com/css2?family=Open+Sans:wght@400;600;700&family=Roboto+Condensed:wght@700&display=swap">
<style>
  :root{
    --paper:#ffffff;
    --panel:#f1f1f1;
    --ink:#1d1d1f;
    --navy:#11112f;
    --brand-ink:#2e3e4e;
    --yellow:#fdc70c;
    --headline-yellow:#fff200;
    --ring:#cfcfcf;
    --icon:#171a3a;
    --white:#ffffff;
  }
  *{margin:0;padding:0;box-sizing:border-box}
  html,body{width:856px;height:1200px;overflow:hidden;background:var(--paper)}
  .flyer{position:relative;width:856px;height:1200px;background:var(--paper);font-family:"Open Sans",Arial,sans-serif;color:var(--ink)}
  .panel{position:absolute;left:13px;top:500px;width:830px;height:584px;background:var(--panel)}
  .band-yellow{position:absolute;left:13px;top:1084px;width:830px;height:18px;background:var(--yellow)}
  .band-navy{position:absolute;left:13px;top:1102px;width:830px;height:84px;background:var(--navy)}
  .curves{position:absolute;left:0;top:0;width:856px;height:660px}
  .brand{position:absolute;left:330px;top:46px;display:flex;align-items:center;gap:10px}
  .brand-dot{width:34px;height:34px;border-radius:50%;background:var(--brand-ink)}
  .brand-text{display:flex;flex-direction:column;align-items:flex-end}
  .brand-name{font-size:32px;font-weight:600;color:var(--brand-ink);line-height:1;letter-spacing:-0.5px}
  .brand-tag{font-size:10px;font-weight:600;color:var(--brand-ink);margin-top:4px}
  .hero-copy{position:absolute;left:390px;top:352px;color:var(--white)}
  .hero-lead{font-size:31px;margin-left:10px;line-height:1.2}
  .hero-big{font-family:"Roboto Condensed","Arial Narrow",sans-serif;font-size:36px;font-weight:700;color:var(--headline-yellow);line-height:1.45;letter-spacing:.3px}
  .hero-sub{font-size:31px;line-height:1.4}
  .testimonial{position:absolute;left:166px;top:632px;width:620px}
  .quote-line{font-size:14px;white-space:nowrap}
  .quote-name{font-size:26px}
  .quote-line2{font-size:14px;margin:22px 0 0 114px}
  .attribution{font-size:14px;margin-top:36px;line-height:1.5}
  .feature{position:absolute;top:806px;text-align:left}
  .feature-ring{width:128px;height:128px;border:3px solid var(--ring);border-radius:50%;display:flex;align-items:center;justify-content:center}
  .feature-title{font-family:"Roboto Condensed","Arial Narrow",sans-serif;font-size:20px;font-weight:700;margin-top:12px}
  .feature-text{font-size:12.5px;line-height:1.35;margin-top:10px}
  .f-contact{left:63px}
  .f-contact .feature-ring{margin-left:10px}
  .f-contact .feature-title{margin-left:16px}
  .f-what{left:330px}
  .f-what .feature-ring{margin-left:17px}
  .f-what .feature-title{margin-left:25px}
  .f-industries{left:600px}
  .f-industries .feature-ring{margin-left:38px}
  .f-industries .feature-text{margin-left:35px}
</style>
</head>
<body>
<main class="flyer">
  <div class="panel"></div>

  <svg class="curves" viewBox="0 0 856 660" aria-hidden="true">
    <path d="M13,80 Q428,160 843,80 L843,100 Q428,190 13,100 Z" fill="var(--yellow)"/>
  </svg>

  <svg class="curves" viewBox="0 0 856 660" role="img" aria-label="Night photograph of a city skyline with illuminated twin towers under a starry sky">
    <defs>
      <linearGradient id="sky" x1="0" y1="0" x2="0" y2="1">
        <stop offset="0" stop-color="#1b2450"/>
        <stop offset=".55" stop-color="#2a2f52"/>
        <stop offset="1" stop-color="#120f14"/>
      </linearGradient>
      <radialGradient id="glow" cx=".12" cy=".55" r=".35">
        <stop offset="0" stop-color="#a8602c" stop-opacity=".75"/>
        <stop offset="1" stop-color="#a8602c" stop-opacity="0"/>
      </radialGradient>
      <radialGradient id="lights" cx=".38" cy=".6" r=".3">
        <stop offset="0" stop-color="#c9a24a" stop-opacity=".45"/>
        <stop offset="1" stop-color="#c9a24a" stop-opacity="0"/>
      </radialGradient>
    </defs>
    <path d="M13,96 Q428,176 843,96 L843,552 Q428,648 13,552 Z" fill="url(#sky)"/>
    <path d="M13,96 Q428,176 843,96 L843,552 Q428,648 13,552 Z" fill="url(#glow)"/>
    <path d="M13,96 Q428,176 843,96 L843,552 Q428,648 13,552 Z" fill="url(#lights)"/>
  </svg>

  <div class="brand">
    <span class="brand-dot"></span>
    <div class="brand-text">
      <span class="brand-name">TalentHarbor</span>
      <span class="brand-tag">Human Resources &amp; Recruitment</span>
    </div>
  </div>

  <div class="hero-copy">
    <p class="hero-lead">We have over</p>
    <p class="hero-big">20 YEARS OF EXPERIENCE</p>
    <p class="hero-sub">Helping companies hire<br>amazing talent</p>
  </div>

  <section class="testimonial">
    <p class="quote-line"><span class="quote-name">“TalentHarbor</span>&nbsp; really delivered on their promise and far exceeded our expectations.</p>
    <p class="quote-line2">Their fixed fee model saved us thousands”</p>
    <p class="attribution">Mark Ellison General Manager<br>Orrin Financial Services</p>
  </section>

  <section class="feature f-contact">
    <div class="feature-ring">
      <svg width="56" height="52" viewBox="0 0 56 52" aria-hidden="true">
        <g fill="var(--icon)">
          <rect x="2" y="34" width="6" height="16"/>
          <rect x="11" y="28" width="6" height="22"/>
          <rect x="20" y="32" width="6" height="18"/>
          <rect x="29" y="24" width="6" height="26"/>
          <rect x="38" y="20" width="6" height="30"/>
          <rect x="47" y="12" width="6" height="38"/>
        </g>
        <polyline points="2,28 14,18 24,24 42,8" fill="none" stroke="var(--icon)" stroke-width="4"/>
        <polygon points="36,3 52,1 50,16" fill="var(--icon)"/>
      </svg>
    </div>
    <h2 class="feature-title">CONTACT US</h2>
    <p class="feature-text">Start a conversation today<br>&nbsp;and see why these companies<br>&nbsp;turn to us time and time again</p>
  </section>

  <section class="feature f-what">
    <div class="feature-ring">
      <svg width="56" height="56" viewBox="0 0 56 56" aria-hidden="true">
        <circle cx="28" cy="28" r="23" fill="none" stroke="var(--icon)" stroke-width="9" stroke-dasharray="9 9.06"/>
        <circle cx="28" cy="28" r="17" fill="var(--icon)"/>
        <circle cx="28" cy="28" r="7" fill="var(--panel)"/>
      </svg>
    </div>
    <h2 class="feature-title">WHAT WE DO</h2>
    <p class="feature-text">We aren’t a recruitment agency,<br>&nbsp;we are an extension of your team.<br>We become your very own HR &amp;<br>Recruitment department to be called<br>&nbsp;upon as and when needed.</p>
  </section>

  <section class="feature f-industries">
    <div class="feature-ring">
      <svg width="56" height="56" viewBox="0 0 56 56" aria-hidden="true">
        <circle cx="28" cy="10" r="6" fill="none" stroke="var(--icon)" stroke-width="4"/>
        <line x1="28" y1="16" x2="28" y2="50" stroke="var(--icon)" stroke-width="5"/>
        <path d="M8,34 Q10,50 28,50 Q46,50 48,34" fill="none" stroke="var(--icon)" stroke-width="5"/>
        <polygon points="2,36 14,36 8,28" fill="var(--icon)"/>
        <polygon points="42,36 54,36 48,28" fill="var(--icon)"/>
      </svg>
    </div>
    <h2 class="feature-title">INDUSTRIES WE SERVE</h2>
    <p class="feature-text">Mining and Oil &amp; Gas<br>Accounting &amp; Finance<br>Sales &amp; Marketing<br>IT &amp; Communications<br>Government &amp; Not for Profit</p>
  </section>

  <div class="band-yellow"></div>
  <div class="band-navy"></div>
</main>
</body>
</html>
```